Wren Sporting Goods Inc.

Need to create a website that is informational and has the ability to sell goods and services. Such as a custom t shirt designer where the user can upload and image to be displayed on the garmet. The sports we specialize in are basketball, football, and baseball.

Would like like:
Home Page
Locker Room Page:
Custom Uniforms Page
Custom Shirt Creator
Brands
About

Competitor websites are
tundrafieldwearnx.com
dvq.com
lumarogear.com

```html
<!DOCTYPE html>
<html lang="en">
<head>
<meta charset="utf-8">
<title>Wren Sporting Goods Inc. — Custom Sports Apparel</title>
<link rel="stylesheet" href="https://fonts.googleapis.com/css2?family=Archivo+Black&family=Inter:wght@400;500;600;700&display=swap">
<style>
:root{
  --orange:#f5731c;
  --orange-soft:#fde9da;
  --navy:#171e2e;
  --navy-2:#222a3b;
  --navy-3:#2c3446;
  --ink:#111827;
  --muted:#5b6472;
  --line:#e6e8ec;
  --bg-soft:#f5f6f8;
  --blue:#1f4fbf;
  --red:#e23a34;
  --green:#1f9d55;
  --white:#ffffff;
}
*{box-sizing:border-box;margin:0;padding:0}
html,body{width:1200px;height:3968px;overflow:hidden}
body{font-family:"Inter",sans-serif;color:var(--ink);background:var(--white);position:relative}
.display{font-family:"Archivo Black",sans-serif;font-weight:400}
header,section,footer{position:absolute;left:0;width:1200px}
.btn{display:inline-flex;align-items:center;justify-content:center;gap:8px;font-weight:600;border-radius:4px;font-size:13px}
.btn-orange{background:var(--orange);color:#fff}
.btn-white{background:#fff;color:var(--ink)}
.pill{display:inline-block;font-size:10px;font-weight:500;border-radius:20px;padding:4px 12px}
.center{text-align:center}

/* nav */
.nav{top:0;height:62px;background:#fff;border-bottom:1px solid var(--line);z-index:2}
.brand{position:absolute;left:80px;top:21px;display:flex;align-items:center;gap:7px;font-weight:700;font-size:11px;color:var(--blue);white-space:nowrap}
.brand .mark{width:18px;height:18px;background:var(--red);border-radius:3px;flex:none}
.nav-links{position:absolute;left:252px;top:25px;display:flex;gap:22px;font-size:11px;font-weight:500;color:#374151}
.nav-links .on{color:var(--ink);font-weight:600}
.nav-icons{position:absolute;left:944px;top:24px;display:flex;gap:16px}
.badge{position:absolute;top:-6px;left:6px;width:12px;height:12px;border-radius:50%;background:var(--orange);color:#fff;font-size:8px;text-align:center;line-height:12px}
.quote{position:absolute;left:1034px;top:18px;width:89px;height:31px;font-size:11px}

/* hero */
.hero{top:62px;height:488px;background:linear-gradient(90deg,#1a2233 0%,#2b3548 45%,#3a455b 70%,#222b3c 100%)}
.hero-photo{position:absolute;inset:0;background:radial-gradient(ellipse at 60% 30%,rgba(120,110,100,.35),transparent 60%),linear-gradient(180deg,rgba(0,0,0,0) 70%,rgba(230,232,240,.9) 100%)}
.hero .pill{position:absolute;left:77px;top:49px;background:rgba(245,115,28,.3);color:#f8b27f;border:1px solid rgba(245,115,28,.5)}
.hero h1{position:absolute;left:77px;top:92px;font-size:54px;line-height:63px;color:#fff}
.hero p{position:absolute;left:77px;top:300px;font-size:17px;color:#e5e7eb}
.hero .b1{position:absolute;left:77px;top:351px;width:188px;height:40px}
.hero .b2{position:absolute;left:276px;top:351px;width:152px;height:40px}
.rating{position:absolute;left:77px;top:426px;display:flex;align-items:center;gap:4px;font-size:11px;font-weight:600;color:#fff}

/* sports */
.sports{top:550px;height:599px;background:var(--bg-soft)}
.sec-title{font-size:34px;color:var(--ink)}
.sec-sub{font-size:14px;color:var(--muted);margin-top:10px}
.sports .head{position:absolute;top:67px;width:1200px}
.sport-cards{position:absolute;left:77px;top:182px;display:flex;gap:22px}
.sport-card{width:334px;height:351px;background:#fff;border-radius:6px;overflow:hidden;position:relative;box-shadow:0 2px 8px rgba(0,0,0,.06)}
.sport-img{height:245px}
.sport-card h3{position:absolute;left:22px;top:268px;font-size:21px;font-weight:700}
.sport-card .dot{position:absolute;right:22px;top:270px;width:20px;height:20px;border-radius:50%}
.sport-card p{position:absolute;left:22px;top:307px;font-size:11px;color:var(--muted)}
.sport-card .bar{position:absolute;left:22px;right:22px;top:338px;height:30px;background:var(--navy);border-radius:4px}

/* design */
.design{top:1149px;height:651px;background:#fff}
.design .pill{position:absolute;left:77px;top:72px;background:var(--orange-soft);color:var(--orange);border:1px solid #f8c8a4}
.design h2{position:absolute;left:77px;top:113px;width:520px;font-size:34px;line-height:34px}
.design .lead{position:absolute;left:77px;top:209px;width:510px;font-size:13.5px;line-height:20px;color:var(--muted)}
.steps{position:absolute;left:77px;top:274px}
.step{display:flex;gap:14px;height:65px}
.step .n{width:32px;height:32px;border-radius:50%;background:var(--orange);color:#fff;font-size:11px;font-weight:700;display:flex;align-items:center;justify-content:center;flex:none}
.step h4{font-size:14px;font-weight:600;margin-top:1px}
.step p{font-size:11px;color:var(--muted);margin-top:7px}
.design .go{position:absolute;left:77px;top:543px;width:171px;height:41px;font-size:13px}
.studio{position:absolute;left:622px;top:117px;width:501px;height:420px;border-radius:16px;background:linear-gradient(135deg,#f6e1d6,#efe6ee 60%,#dcdcef)}
.studio-screen{position:absolute;left:56px;top:17px;width:388px;height:385px;background:linear-gradient(180deg,#2a2a2e 0 12%,#8b8f99 12% 88%,#2a2a2e 88%)}

/* locker */
.locker{top:1800px;height:629px;background:var(--navy)}
.locker .head{position:absolute;top:67px;width:1200px;color:#fff}
.locker .sec-title{color:#fff}
.locker .sec-sub{color:#aab1bf}
.kits{position:absolute;left:77px;top:179px;display:flex;gap:22px}
.kit{width:334px;height:304px;background:var(--navy-2);border-radius:6px;padding:17px;position:relative}
.kit-img{height:179px;border-radius:3px}
.kit h3{font-size:14.5px;font-weight:700;color:#fff;margin-top:13px}
.kit .meta{font-size:11px;color:#9aa2b1;margin-top:6px}
.kit .row{display:flex;gap:10px;margin-top:11px}
.kit .edit{flex:1;height:26px;font-size:11px}
.kit .more{width:26px;height:26px;background:var(--navy-3);border-radius:4px;display:flex;align-items:center;justify-content:center}
.enter{position:absolute;left:504px;top:518px;width:192px;height:41px;font-size:12px}

/* partners */
.partners{top:2429px;height:251px;background:#fff;border-bottom:1px solid var(--line)}
.partners .label{position:absolute;top:55px;width:1200px;font-size:9.5px;letter-spacing:1px;color:var(--muted)}
.partners h2{position:absolute;top:80px;width:1200px;font-size:21px;font-weight:600}
.partner{position:absolute;top:145px;width:46px;height:46px;border-radius:3px;background:#8d929b}

/* why */
.why{top:2680px;height:616px;background:var(--bg-soft)}
.why .head{position:absolute;top:67px;width:1200px}
.why-cards{position:absolute;left:77px;top:180px;display:flex;gap:22px}
.why-card{width:245px;height:202px;background:#fff;border-radius:6px;text-align:center;padding-top:24px;box-shadow:0 1px 6px rgba(0,0,0,.05)}
.why-card .ic{width:56px;height:56px;border-radius:50%;margin:0 auto;display:flex;align-items:center;justify-content:center}
.why-card h3{font-size:16.5px;font-weight:600;margin-top:20px}
.why-card p{font-size:11px;line-height:16px;color:var(--muted);margin:12px 24px 0}
.stats{position:absolute;left:77px;top:426px;width:1046px;height:124px;background:#fff;border-radius:6px;display:flex;box-shadow:0 1px 6px rgba(0,0,0,.05)}
.stat{flex:1;text-align:center;padding-top:30px}
.stat b{font-family:"Archivo Black",sans-serif;font-weight:400;font-size:33px;display:block}
.stat span{font-size:11px;color:#374151;font-weight:500;display:block;margin-top:6px}

/* cta */
.cta{top:3296px;height:374px;background:linear-gradient(180deg,#232b3d,#2b3447)}
.cta h2{position:absolute;top:68px;width:1200px;font-size:44px;color:#fff}
.cta p{position:absolute;top:138px;left:340px;width:520px;font-size:16px;line-height:23px;color:#dfe3ea}
.cta .btn{position:absolute;left:516px;top:208px;width:166px;height:45px;font-size:14px}
.contact{position:absolute;top:290px;width:1200px;display:flex;justify-content:center;gap:24px;font-size:11px;font-weight:500;color:#fff}
.contact span{display:flex;align-items:center;gap:6px}

/* footer */
.footer{top:3670px;height:298px;background:var(--navy)}
.footer .brand{left:77px;top:46px;color:#6f93e8}
.footer .about{position:absolute;left:77px;top:90px;width:390px;font-size:11px;line-height:17px;color:#b3bac6}
.socials{position:absolute;left:77px;top:139px;display:flex;gap:14px}
.socials i{width:24px;height:24px;border-radius:50%;background:var(--navy-3);display:block}
.col{position:absolute;top:46px}
.col h4{font-size:11px;font-weight:700;color:#fff;margin-bottom:12px}
.col a{display:block;font-size:11px;color:#b3bac6;text-decoration:none;line-height:22.5px}
.copy{position:absolute;left:77px;top:241px;font-size:9.5px;color:#b3bac6}
.pay{position:absolute;left:936px;top:234px;display:flex;gap:12px}
.pay i{width:24px;height:17px;border-radius:2px;background:#9aa1ad;display:block}
.footer .rule{position:absolute;left:77px;top:216px;width:1046px;height:1px;background:var(--navy-3)}
</style>
</head>
<body>

<header class="nav">
  <div class="brand"><span class="mark"></span>Wren Sporting Goods</div>
  <nav class="nav-links"><span class="on">Shop</span><span>Customize</span><span>Locker Room</span><span>Team Orders</span><span>About</span></nav>
  <div class="nav-icons">
    <svg width="14" height="14" viewBox="0 0 24 24" fill="none" stroke="#374151" stroke-width="2.4"><circle cx="11" cy="11" r="7"/><path d="M20 20l-4-4"/></svg>
    <span style="position:relative"><svg width="14" height="14" viewBox="0 0 24 24" fill="none" stroke="#374151" stroke-width="2.4"><path d="M3 4h3l2 11h11l2-8H7"/><circle cx="9" cy="20" r="1.5"/><circle cx="18" cy="20" r="1.5"/></svg><span class="badge">0</span></span>
    <svg width="14" height="14" viewBox="0 0 24 24" fill="none" stroke="#374151" stroke-width="2.4"><circle cx="12" cy="8" r="4"/><path d="M4 21c1-5 15-5 16 0"/></svg>
  </div>
  <a class="btn btn-orange quote">Get Quote</a>
</header>

<section class="hero">
  <div class="hero-photo" role="img" aria-label="Basketball players in action during a game"></div>
  <span class="pill">Trusted by 500+ Teams</span>
  <h1 class="display">Custom Sports<br>Apparel<br>&amp; Team Uniforms</h1>
  <p>Designed for teams. Built for performance.</p>
  <a class="btn btn-orange b1">Shop Custom Uniforms</a>
  <a class="btn btn-white b2">Design Your Shirt</a>
  <div class="rating">
    <svg width="86" height="15" viewBox="0 0 86 15" fill="#fbbf24"><g id="st"><path d="M7.5 0l2.2 4.7 5 .6-3.7 3.4 1 5-4.5-2.5L3 13.7l1-5L.3 5.3l5-.6z"/></g><use href="#st" x="18"/><use href="#st" x="36"/><use href="#st" x="54"/><use href="#st" x="72"/></svg>
    <span style="margin-left:4px">4.9/5 from 2,500+ reviews</span>
  </div>
</section>

<section class="sports">
  <div class="head center"><h2 class="sec-title display">Shop by Sport</h2><p class="sec-sub">Premium uniforms for every game</p></div>
  <div class="sport-cards">
    <article class="sport-card">
      <div class="sport-img" role="img" aria-label="Basketball player in an orange uniform on court" style="background:linear-gradient(180deg,#3a2a24,#b4541e 60%,#2a2420)"></div>
      <h3>Basketball</h3><span class="dot" style="background:var(--orange)"></span>
      <p>Custom jerseys, shorts &amp; warm-ups</p><div class="bar"></div>
    </article>
    <article class="sport-card">
      <div class="sport-img" role="img" aria-label="Football player in a red uniform on the field" style="background:linear-gradient(180deg,#b9bcc2,#c9cdd2 45%,#5e8a3a 75%,#4c7a2e)"></div>
      <h3>Football</h3><span class="dot" style="background:var(--red)"></span>
      <p>Complete team kits &amp; equipment</p><div class="bar"></div>
    </article>
    <article class="sport-card">
      <div class="sport-img" role="img" aria-label="Baseball player in a blue jersey at the ballpark" style="background:linear-gradient(180deg,#1f3a4f,#4a6b56 60%,#3857a8 85%)"></div>
      <h3>Baseball</h3><span class="dot" style="background:var(--blue)"></span>
      <p>Jerseys, pants &amp; accessories</p><div class="bar"></div>
    </article>
  </div>
</section>

<section class="design">
  <span class="pill">Easy Customization</span>
  <h2 class="display">Design Your Perfect Team Kit</h2>
  <p class="lead">Create uniforms that represent your team's identity with our simple 4-step process</p>
  <div class="steps">
    <div class="step"><span class="n">1</span><div><h4>Choose Your Garment</h4><p>Select from jerseys, shorts, pants, and accessories</p></div></div>
    <div class="step"><span class="n">2</span><div><h4>Upload Logo &amp; Design</h4><p>Add your team logo, mascot, or custom graphics</p></div></div>
    <div class="step"><span class="n">3</span><div><h4>Customize Colors &amp; Text</h4><p>Match your team colors and add player names &amp; numbers</p></div></div>
    <div class="step"><span class="n">4</span><div><h4>Order in Bulk</h4><p>Get team pricing and fast turnaround on large orders</p></div></div>
  </div>
  <a class="btn btn-orange go">Start Designing
    <svg width="12" height="12" viewBox="0 0 24 24" fill="none" stroke="#fff" stroke-width="2.6"><path d="M4 12h15M13 6l6 6-6 6"/></svg></a>
  <div class="studio"><div class="studio-screen" role="img" aria-label="Shirt design tool showing a red jersey with colour picker"></div></div>
</section>

<section class="locker">
  <div class="head center"><h2 class="sec-title display">Your Team Locker Room</h2><p class="sec-sub">Manage designs, orders, and team rosters in one place</p></div>
  <div class="kits">
    <article class="kit">
      <div class="kit-img" role="img" aria-label="Black and orange basketball kit, front and back" style="background:linear-gradient(90deg,#fff,#2a2a2a 30%,#e56a1c 45%,#1a1a1a 70%,#fff)"></div>
      <h3>Warriors Kit 2024</h3><p class="meta">Basketball • 15 players</p>
      <div class="row"><a class="btn btn-orange edit">Edit Design</a><span class="more"><svg width="3" height="11"><circle cx="1.5" cy="1.5" r="1.3" fill="#ccc"/><circle cx="1.5" cy="5.5" r="1.3" fill="#ccc"/><circle cx="1.5" cy="9.5" r="1.3" fill="#ccc"/></svg></span></div>
    </article>
    <article class="kit">
      <div class="kit-img" role="img" aria-label="Red and white football kit with pants and accessories" style="background:linear-gradient(90deg,#2e2e30,#d8d8d8 20%,#d42a2a 40%,#e8e8e8 65%,#c22 85%,#2e2e30)"></div>
      <h3>Titans Kit 2024</h3><p class="meta">Football • 22 players</p>
      <div class="row"><a class="btn btn-orange edit">Edit Design</a><span class="more"><svg width="3" height="11"><circle cx="1.5" cy="1.5" r="1.3" fill="#ccc"/><circle cx="1.5" cy="5.5" r="1.3" fill="#ccc"/><circle cx="1.5" cy="9.5" r="1.3" fill="#ccc"/></svg></span></div>
    </article>
    <article class="kit">
      <div class="kit-img" role="img" aria-label="Blue and grey baseball kit, front and back" style="background:linear-gradient(90deg,#fff,#2563c9 25%,#b8bcc4 50%,#c6cad1 75%,#fff)"></div>
      <h3>Eagles Kit 2024</h3><p class="meta">Baseball • 18 players</p>
      <div class="row"><a class="btn btn-orange edit">Edit Design</a><span class="more"><svg width="3" height="11"><circle cx="1.5" cy="1.5" r="1.3" fill="#ccc"/><circle cx="1.5" cy="5.5" r="1.3" fill="#ccc"/><circle cx="1.5" cy="9.5" r="1.3" fill="#ccc"/></svg></span></div>
    </article>
  </div>
  <a class="btn btn-white enter">Enter Locker Room
    <svg width="12" height="12" viewBox="0 0 24 24" fill="none" stroke="#111" stroke-width="2.6"><path d="M4 12h15M13 6l6 6-6 6"/></svg></a>
</section>

<section class="partners">
  <p class="label center">TRUSTED PARTNERS</p>
  <h2 class="center">Official Licensed Products</h2>
  <span class="partner" style="left:125px;background:#c9ccd2"></span>
  <span class="partner" style="left:307px"></span>
  <span class="partner" style="left:487px"></span>
  <span class="partner" style="left:667px"></span>
  <span class="partner" style="left:847px"></span>
  <span class="partner" style="left:1026px"></span>
</section>

<section class="why">
  <div class="head center"><h2 class="sec-title display">Why Teams Choose Us</h2><p class="sec-sub">The winning combination for your team's success</p></div>
  <div class="why-cards">
    <div class="why-card"><div class="ic" style="background:#fdebdd"><svg width="20" height="20" viewBox="0 0 24 24" fill="none" stroke="var(--orange)" stroke-width="2.4"><circle cx="12" cy="9" r="5"/><path d="M9 14l-2 7 5-3 5 3-2-7"/></svg></div><h3>Custom Quality</h3><p>Premium fabrics and professional-grade printing that lasts season after season</p></div>
    <div class="why-card"><div class="ic" style="background:#e3e9fb"><svg width="20" height="20" viewBox="0 0 24 24" fill="var(--blue)"><path d="M13 2L4 14h7l-1 8 9-12h-7z"/></svg></div><h3>Fast Turnaround</h3><p>Rush orders available with 7-10 day production on most custom uniforms</p></div>
    <div class="why-card"><div class="ic" style="background:#fde2e1"><svg width="20" height="20" viewBox="0 0 24 24" fill="var(--red)"><path d="M3 12l9-9h9v9l-9 9z"/><circle cx="16" cy="8" r="1.6" fill="#fde2e1"/></svg></div><h3>Team Pricing</h3><p>Volume discounts and flexible payment options for teams of all sizes</p></div>
    <div class="why-card"><div class="ic" style="background:#dff3e7"><svg width="20" height="20" viewBox="0 0 24 24" fill="none" stroke="var(--green)" stroke-width="2.4"><path d="M12 3l8 3v6c0 5-4 8-8 9-4-1-8-4-8-9V6z"/><path d="M9 12l2 2 4-4"/></svg></div><h3>Trusted by 500+</h3><p>Schools, leagues, and clubs nationwide trust us for their team gear</p></div>
  </div>
  <div class="stats">
    <div class="stat"><b style="color:var(--orange)">500+</b><span>Teams Outfitted</span></div>
    <div class="stat"><b style="color:var(--blue)">50K+</b><span>Uniforms Delivered</span></div>
    <div class="stat"><b style="color:var(--red)">4.9★</b><span>Average Rating</span></div>
    <div class="stat"><b style="color:var(--green)">7-10</b><span>Day Turnaround</span></div>
  </div>
</section>

<section class="cta" role="img" aria-label="Team celebrating together, darkened background">
  <h2 class="display center">Outfit Your Team Today</h2>
  <p class="center">Join hundreds of teams who trust us for quality uniforms and exceptional service</p>
  <a class="btn btn-orange">Get Started
    <svg width="12" height="12" viewBox="0 0 24 24" fill="none" stroke="#fff" stroke-width="2.6"><path d="M4 12h15M13 6l6 6-6 6"/></svg></a>
  <div class="contact">
    <span><svg width="11" height="11" viewBox="0 0 24 24" fill="var(--orange)"><path d="M6 2l4 4-2 3c1 3 4 6 7 7l3-2 4 4-3 4C10 21 3 14 2 5z"/></svg>1-800-555-0148</span>
    <span><svg width="11" height="11" viewBox="0 0 24 24" fill="var(--orange)"><path d="M2 5h20v14H2z"/><path d="M2 5l10 8 10-8" stroke="#2a3346" stroke-width="2" fill="none"/></svg>orders@wrensporting.com</span>
    <span><svg width="11" height="11" viewBox="0 0 24 24"><circle cx="12" cy="12" r="10" fill="var(--orange)"/><path d="M12 6v6l4 2" stroke="#2a3346" stroke-width="2.4" fill="none"/></svg>Mon-Fri 8AM-6PM EST</span>
  </div>
</section>

<footer class="footer">
  <div class="brand"><span class="mark"></span>Wren Sporting Goods</div>
  <p class="about">Premium custom sports apparel and team uniforms for athletes, schools, and leagues nationwide.</p>
  <div class="socials"><i></i><i></i><i></i><i></i></div>
  <div class="col" style="left:508px"><h4>Shop</h4><a>Basketball</a><a>Football</a><a>Baseball</a><a>Soccer</a><a>Accessories</a></div>
  <div class="col" style="left:724px"><h4>Resources</h4><a>Design Guide</a><a>Size Charts</a><a>Team Orders</a><a>FAQ</a><a>Contact Us</a></div>
  <div class="col" style="left:941px"><h4>Company</h4><a>About Us</a><a>Testimonials</a><a>Careers</a><a>Privacy Policy</a><a>Terms of Service</a></div>
  <div class="rule"></div>
  <p class="copy">© 2024 Wren Sporting Goods. All rights reserved.</p>
  <div class="pay"><i></i><i></i><i></i><i></i><i></i></div>
</footer>

</body>
</html>
```